T&K Holdings

Design a modern simple business card. I have attached a clean version of a card we like form Harbor Pines another company we own. I also attached the old T&K card design and logo and a couple of ideas we had but just can't finalize on whether we like them or not. We would like to include the 20 year logo somewhere on the card.

```html
<!DOCTYPE html>
<html lang="en">
<head>
<meta charset="utf-8">
<title>T&amp;K Holdings — Business Card</title>
<link href="https://fonts.googleapis.com/css2?family=Arimo:wght@400;700&display=swap" rel="stylesheet">
<style>
  :root {
    --navy: #1e1b56;
    --grey-text: #55565a;
    --grey-light: #8a8b8f;
    --paper: #efefee;
    --white: #f4f4f4;
    --backdrop: #6b6b6b;
    --edge: #3ab7de;
  }
  * { box-sizing: border-box; margin: 0; padding: 0; }
  html, body {
    width: 1200px; height: 988px; overflow: hidden;
    background: var(--backdrop);
    font-family: "Arimo", Arial, sans-serif;
  }
  .sheet {
    width: 1200px; height: 988px;
    display: flex; flex-direction: column; align-items: center; justify-content: center;
    gap: 40px;
  }
  .card {
    width: 760px; height: 434px;
    border-radius: 26px;
    display: flex; align-items: center;
    box-shadow: 0 0 0 2px var(--edge);
    position: relative;
  }
  .card--front { background: var(--paper); }
  .card--back { background: var(--navy); }

  .brand {
    width: 340px; display: flex; align-items: center; justify-content: center; gap: 14px;
  }
  .brand__dot { width: 22px; height: 22px; border-radius: 50%; }
  .brand__name { font-weight: 700; font-size: 74px; letter-spacing: -1px; }
  .card--front .brand__dot { background: var(--navy); }
  .card--front .brand__name { color: var(--navy); }
  .card--back .brand__dot { background: var(--white); }
  .card--back .brand__name { color: var(--white); }

  .divider { width: 2px; height: 250px; }
  .card--front .divider { background: var(--navy); }
  .card--back .divider { width: 1px; background: var(--white); opacity: .8; }

  .details { padding-left: 34px; color: var(--grey-text); }
  .details__name { font-weight: 700; font-size: 34px; color: var(--navy); line-height: 1.05; }
  .details__title { font-size: 21px; color: var(--grey-light); margin-bottom: 14px; }
  .details__company { font-weight: 700; font-size: 19px; color: var(--navy); }
  .details__address { font-size: 19px; line-height: 1.3; margin-bottom: 12px; }
  .contact { list-style: none; font-size: 19px; line-height: 1.45; }
  .contact li { display: flex; align-items: center; gap: 12px; }
  .contact svg { width: 15px; height: 15px; fill: var(--navy); flex: none; }

  .anniversary { padding-left: 40px; color: var(--white); }
  .anniversary__number { font-size: 130px; font-weight: 700; line-height: .9; letter-spacing: -4px; }
  .anniversary__label { font-size: 26px; font-weight: 700; letter-spacing: 4px; margin-top: 6px; }
  .anniversary__years { font-size: 26px; font-weight: 700; letter-spacing: 2px; margin-top: 4px; }
</style>
</head>
<body>
<main class="sheet">

  <section class="card card--front">
    <div class="brand">
      <span class="brand__dot"></span>
      <span class="brand__name">T&amp;K</span>
    </div>
    <div class="divider"></div>
    <div class="details">
      <p class="details__name">Dylan Marsh</p>
      <p class="details__title">IT Director</p>
      <p class="details__company">T&amp;K Holdings</p>
      <p class="details__address">218 Cedar Avenue, Suite 410<br>Lakeview, TX 75820</p>
      <ul class="contact">
        <li><svg viewBox="0 0 16 16"><path d="M3.5 1l2.5 3-1.5 1.5c.8 2 2.5 3.7 4.5 4.5L10.5 8.5l3 2.5-1.5 3C7 14 2 9 2 2.5z"/></svg>555-214-3870</li>
        <li><svg viewBox="0 0 16 16"><path d="M4 1h8v14H4zM5.5 2.5v9h5v-9zM7 12.5h2v1H7z"/></svg>555-386-4127</li>
        <li><svg viewBox="0 0 16 16"><path d="M1 3h14v10H1zM2.5 4.5 8 9l5.5-4.5z"/></svg>dmarsh@tkholdings.com</li>
        <li><svg viewBox="0 0 16 16"><path d="M8 1a7 7 0 1 0 0 14A7 7 0 0 0 8 1zm0 1.6c.9 1 1.5 2.4 1.7 3.9H6.3C6.5 5 7.1 3.6 8 2.6zM2.7 7.5h2.1c.1 1.5.6 2.9 1.4 4A5.4 5.4 0 0 1 2.7 7.5zm6.9 4.2c.8-1.1 1.3-2.5 1.5-4.2h2.2a5.4 5.4 0 0 1-3.7 4.2z"/></svg>www.tkholdings.com</li>
      </ul>
    </div>
  </section>

  <section class="card card--back">
    <div class="brand">
      <span class="brand__dot"></span>
      <span class="brand__name">T&amp;K</span>
    </div>
    <div class="divider"></div>
    <div class="anniversary">
      <p class="anniversary__number">20</p>
      <p class="anniversary__label">YEARS</p>
      <p class="anniversary__years">2004-2024</p>
    </div>
  </section>

</main>
</body>
</html>
```